Flyer für ambulanten Pflegedienst
Zielgruppe
Ambulanter Pflegedienst in Gründung. Habe schon ein Logo und Text. Zielgruppe sind Pflege und Hilfsbedürftige Menschen

```html
<!DOCTYPE html>
<html lang="de">
<head>
<meta charset="utf-8">
<title>Lindenhof Ambulant – Flyer</title>
<link href="https://fonts.googleapis.com/css2?family=Libre+Baskerville:wght@400;700&family=Fira+Sans+Condensed:wght@400;500&display=swap" rel="stylesheet">
<style>
:root{
  --bg:#ececec;
  --paper:#ffffff;
  --teal:#4fb0aa;
  --teal-dark:#3a9ab0;
  --heading:#3f9db4;
  --text:#2b2b2b;
  --band-a:#3c98b2;
  --band-b:#57b9b1;
  --photo-a:#d9cfc4;
  --photo-b:#b9ada2;
}
*{margin:0;padding:0;box-sizing:border-box}
html,body{width:1200px;height:628px;overflow:hidden;background:var(--bg)}
body{position:relative;font-family:"Fira Sans Condensed",sans-serif;color:var(--text)}
.page{position:absolute;background:var(--paper);overflow:hidden}
.spread{left:34px;top:27px;width:707px;height:547px}
.single{left:796px;top:27px;width:348px;height:547px}
.gutter{position:absolute;left:348px;top:0;width:24px;height:100%;background:linear-gradient(90deg,rgba(0,0,0,0),rgba(0,0,0,.06),rgba(0,0,0,0))}
.abs{position:absolute}
h2{font-family:"Libre Baskerville",serif;font-weight:400;color:var(--heading);font-size:12.5px;line-height:15px}
.sub{font-family:"Libre Baskerville",serif;color:var(--heading);font-size:8.5px;margin-top:1px}
.lead{font-weight:500;color:var(--teal-dark);font-size:8px;line-height:13px;margin-top:7px}
.body{font-size:8px;line-height:13px;margin-top:7px}
.just{text-align:justify}
.list{font-size:8px;line-height:13px;margin-top:16px;list-style:none}
.right{text-align:right}
.band{position:absolute;left:0;bottom:0;width:100%;height:28px;background:linear-gradient(90deg,var(--band-a),var(--band-b));color:#fff;font-weight:500;font-size:8.6px;line-height:28px;padding:0 24px}
.band .r{position:absolute;right:26px;top:0}
.photo{position:absolute;border-radius:50%;background:radial-gradient(circle at 45% 40%,var(--photo-a),var(--photo-b))}
.bubble{position:absolute;border-radius:50%;background:var(--teal);color:#fff;display:flex;align-items:center;justify-content:center;text-align:center}
.goal{font-weight:500;font-size:8.4px;line-height:14px}
.promise{font-family:"Libre Baskerville",serif;font-size:8.4px;line-height:13px}
.brand{position:absolute;left:24px;top:372px;display:flex;align-items:center;gap:12px}
.brand-dot{width:40px;height:40px;border-radius:50%;background:var(--teal)}
.brand-name{font-family:"Fira Sans Condensed",sans-serif;font-weight:500;color:var(--teal-dark);font-size:28px;line-height:32px}
</style>
</head>
<body>

<section class="page spread">
  <div class="photo" style="left:316px;top:-44px;width:230px;height:230px" role="img" aria-label="Foto: Pflegerin kämmt einer Seniorin die Haare"></div>
  <div class="photo" style="left:503px;top:349px;width:268px;height:268px" role="img" aria-label="Foto: Pflegerin und Seniorin schauen gemeinsam auf ein Tablet"></div>
  <div class="gutter"></div>

  <div class="abs" style="left:24px;top:28px;width:136px">
    <h2>Palliativ Pflege</h2>
    <p class="lead">Erfolgt in enger Zusammenarbeit mit speziell ausgebildeten Ärzten, mit der Palliativ Care (SAPV) Koordinierungsstelle und Seelsorge.</p>
    <p class="lead" style="margin-top:13px">Konzentriert sich auf die professionelle Versorgung und Begleitung im letzten Abschnitt des Lebens.</p>
  </div>

  <div class="abs" style="left:194px;top:24px;width:108px">
    <h2>Verhinderungs-<br>pflege</h2>
    <p class="lead">Das Angebot im Bereich der Verhinderungspflege richtet sich an die Angehörigen, die bei der Pflege stundenweise Entlastung benötigen. Typische Anlässe sind z.B.</p>
    <ul class="list"><li>Krankheit</li><li>Überlastung</li><li>Urlaub</li></ul>
  </div>

  <div class="abs" style="left:24px;top:244px;width:142px">
    <h2>Betreuungs- und<br>Entlastungsleistungen</h2>
    <p class="sub">nach § 45 SGB XI</p>
    <p class="lead" style="margin-top:9px">Voraussetzung ist das Vorliegen eines Pflegegrades. Bei der Antragsstellung eines Pflegegrades sind wir behilflich und begleiten die Begutachtung durch den Medizinischen Dienst der Krankenkasse.</p>
    <ul class="list" style="margin-top:15px">
      <li style="line-height:11px">Unterstützung bei der<br>Haushaltsführung</li><li>Einkaufen</li><li>Begleitung zu Ärzten</li><li>Arzttermine vereinbaren</li><li style="line-height:11px">Unterstützung beim Ausfüllen<br>von Formularen und Anträgen</li><li>Spaziergänge</li>
    </ul>
  </div>

  <div class="abs" style="left:194px;top:244px;width:136px">
    <h2>Alltagsbegleitung</h2>
    <p class="lead">In er Alltagsbegleitung werden die Pflegepersonen in allen alltäglichen Tätigkeiten und Freizeitaktivitäten unterstützen und begleiten. Typische Leistungen sind z.B.</p>
    <ul class="list" style="margin-top:14px">
      <li>Arztbesuche</li><li>Behördengänge</li><li>Kulturelle Veranstaltungen</li><li>Spaziergänge</li><li>Ausflüge</li><li>Wanderungen</li><li>Stadtbummel</li><li>Restaurantbesuche</li><li>Friseurbesuche</li><li>Gedächtnistraining usw.</li>
    </ul>
  </div>

  <div class="abs right" style="left:545px;top:28px;width:140px">
    <h2>Unser Konzept</h2>
    <p class="lead" style="margin-top:6px">Der grundlegende Geschäftsprozess des Unternehmens gliedert sich in die Bereiche Beratung, Pflegekonzept, Vertragsabschluss und Pflege:</p>
  </div>

  <div class="bubble goal" style="left:456px;top:97px;width:112px;height:112px">Das oberste<br>Ziel der Pflege<br>ist die Sicherung und<br>Verbesserung der<br>Lebensqualität.</div>

  <div class="abs" style="left:388px;top:211px;width:140px">
    <h2>Beratung</h2>
    <p class="body just">Kunden werden ausführlich unter Berücksichtigung ihrer Wünsche und Vorstellungen beraten. Denn das vorhandene Pflegeangebot bietet eine Vielzahl an Möglichkeiten. Wichtig ist der Aufbau von Vertrauen.</p>
    <h2 style="margin-top:14px">Pflegekonzept</h2>
    <p class="body just">Unter Berücksichtigung aller Möglichkeiten und Patientenwünsche wird ein individuelles Leistungsangebot entwickelt und eine verbindliche Kostenaufstellung erstellt.</p>
    <h2 style="margin-top:14px">Vertragsabschluss</h2>
    <p class="body">Alle Aufträge mit Kunden werden in schriftlicher Form geschlossen und beidseitig unterzeichnet.</p>
  </div>

  <div class="abs" style="left:552px;top:212px;width:140px">
    <h2>Pflege</h2>
    <p class="body just">Die vereinbarten Pflegeleistungen werden nun umgesetzt. Dabei kann der Kunde stets eine hohe Ausführungsqualität erwarten. Es wird für jeden Kunden eine Mappe zur Pflegedokumentation geführt (Pflegesoftware, die stets vom Kunden sowie seinen Angehörigen eingesehen werden kann).</p>
  </div>

  <div class="band">Ihr Altenpflege- und Seniorenbetreuungsdienst mit Herz<span class="r">Wir nehmen uns Zeit für Ihre Anliegen</span></div>
</section>

<section class="page single">
  <div class="photo" style="left:5px;top:-8px;width:210px;height:210px" role="img" aria-label="Foto: junge Frau und Seniorin beim gemeinsamen Kaffeetrinken"></div>
  <div class="bubble promise" style="left:186px;top:65px;width:142px;height:142px">Wir sorgen dafür,<br>dass Sie zu Hause<br>professionell betreut<br>werden - denn in einer<br>vertrauten Umgebung<br>werden Kranke<br>oft schneller<br>gesünder.</div>

  <div class="abs" style="left:24px;top:214px;width:302px">
    <h2>Gerne helfen wir Ihnen weiter</h2>
    <p class="body just" style="margin-top:8px">Der Altenpflege- und Seniorenbetreuungsdienst führt sämtliche Pflegeleistungen kompetent, professionell und zuverlässig aus. Das oberste Ziel der Pflege ist die Sicherung und Verbesserung der Lebensqualität und das Bewahren des gewohnten Lebensumfelds der Pflegepersonen.<br>Krankenhaus- und Bereuungsheimaufenthalte sollen möglichst vermieden werden. Diesen Grundgedanken liegt die Erkenntnis zu Grunde, dass <b>in einer vertrauten Umgebung Kranke oft schneller gesünder werden</b> und gerade ältere Menschen sich zu Hause besonders wohl und geborgen fühlen.</p>
  </div>

  <div class="brand">
    <div class="brand-dot"></div>
    <div class="brand-name">Lindenhof Ambulant</div>
  </div>

  <div class="band">Ihr Altenpflege- und Seniorenbetreuungsdienst mit Herz</div>
</section>

</body>
</html>
```